Tidal Crumb Ingredients

Ingredients list/einkorn info. We are looking to improve a 5.5 x 8.5" double sided handout (2 per 8.5 x 11" piece of paper) to hand out with bread and for marketing. Or skinnier 3 per piece of paper? Or suggest a better format. Also to be used in social media and web. And possibly a banner.

Target Market(s)

Healthy, intelligent, yoga, athletic, wealthy

Industry/Entity Type

Bakery

Font styles to use
Sans Serif
Other font styles liked:
• simple readable attractive

Requirements
Must have
• Display the value (and uniqueness) of ingredients
Nice to have
• Well presented info with instant visual appeal. Choose between the 2 logos which you like most. Let us know if you want more photos.
Should not have
• Ornate frills

```html
<!DOCTYPE html>
<html lang="en">
<head>
<meta charset="utf-8">
<title>Tidal Crumb – The transformation of bread</title>
<link rel="stylesheet" href="https://fonts.googleapis.com/css2?family=Damion&family=Montserrat:wght@400;500;600;700&family=Roboto+Slab:wght@600;700&display=swap">
<style>
  :root {
    --cream: #fdf1e6;
    --peach: #f4c9a6;
    --orange: #f3873a;
    --orange-deep: #e8702a;
    --rust: #d9652a;
    --brown: #6a2f16;
    --brown-script: #7a3418;
    --navy: #1a4390;
    --ink: #3a2a22;
    --amber: #e07b27;
    --tick: #e8a04c;
    --white: #ffffff;
    --seam: #e9c4a4;
  }
  * { box-sizing: border-box; margin: 0; padding: 0; }
  html, body {
    width: 723px;
    height: 1200px;
    overflow: hidden;
    background: var(--cream);
  }
  .sheet {
    display: grid;
    grid-template-columns: 361.5px 361.5px;
    grid-template-rows: 600px 600px;
    width: 723px;
    height: 1200px;
  }
  .panel {
    position: relative;
    overflow: hidden;
    background: radial-gradient(ellipse 75% 60% at 50% 40%, #fffaf4 0%, var(--cream) 45%, var(--peach) 100%);
    font-family: "Montserrat", sans-serif;
    color: var(--ink);
    text-align: center;
    border-right: 1px solid var(--seam);
  }
  .panel:nth-child(2n) { border-right: none; }
  .content {
    position: relative;
    z-index: 2;
    padding: 16px 18px 0;
  }
  .script-title {
    font-family: "Damion", cursive;
    font-weight: 400;
    font-size: 26px;
    color: var(--brown-script);
    line-height: 1.15;
  }
  .brand {
    display: flex;
    align-items: center;
    justify-content: center;
    gap: 7px;
    margin: 10px 0 12px;
  }
  .brand-dot {
    width: 13px;
    height: 13px;
    border-radius: 50%;
    background: var(--navy);
  }
  .brand-name {
    font-weight: 700;
    font-size: 15px;
    letter-spacing: 1.5px;
    color: var(--navy);
    text-transform: uppercase;
  }
  .headline {
    font-family: "Roboto Slab", serif;
    font-weight: 700;
    font-size: 14.5px;
    color: var(--navy);
    word-spacing: 5px;
    line-height: 1.1;
    white-space: nowrap;
  }
  .subline {
    font-family: "Roboto Slab", serif;
    font-weight: 600;
    font-size: 9.8px;
    color: var(--navy);
    margin-top: 1px;
    white-space: nowrap;
  }
  .section-label {
    font-family: "Damion", cursive;
    font-weight: 400;
    font-size: 15px;
    color: var(--brown-script);
    margin-top: 12px;
    line-height: 1.1;
  }
  .section-text {
    font-size: 8.4px;
    line-height: 1.4;
    margin-top: 4px;
  }
  .split {
    display: flex;
    margin-top: 12px;
  }
  .split-col { flex: 1; }
  .split-col .section-label { margin-top: 0; }
  .split-divider {
    width: 1px;
    background: var(--ink);
    opacity: 0.6;
  }
  .extras {
    margin: 14px auto 0;
    width: 300px;
    padding: 6px 10px;
    border-radius: 8px;
    background: var(--brown);
    color: var(--white);
    font-weight: 700;
    font-size: 8.2px;
    line-height: 1.35;
  }
  .tolerance {
    font-family: "Roboto Slab", serif;
    font-weight: 600;
    font-size: 8.2px;
    color: var(--amber);
    margin-top: 10px;
  }
  .note {
    font-size: 6.8px;
    margin-top: 6px;
  }

  .intro {
    font-size: 8.4px;
    line-height: 1.35;
    margin-top: 5px;
  }
  .intro strong { font-weight: 700; }
  .back .section-label {
    text-align: left;
    margin-top: 10px;
  }
  .benefits {
    list-style: none;
    text-align: left;
    margin-top: 8px;
  }
  .benefits li {
    position: relative;
    padding-left: 12px;
    font-size: 7.9px;
    line-height: 1.3;
    margin-bottom: 4.2px;
  }
  .benefits svg {
    position: absolute;
    left: 0;
    top: 2px;
    width: 7px;
    height: 7px;
  }
  .gluten-box {
    margin: 10px auto 0;
    width: 210px;
    padding: 5px 8px;
    border-radius: 7px;
    background: var(--brown);
    color: var(--white);
    font-family: "Roboto Slab", serif;
    font-weight: 600;
    font-size: 10.5px;
    line-height: 1.15;
  }

  .landscape {
    position: absolute;
    left: 0;
    bottom: 0;
    width: 100%;
    height: 250px;
    z-index: 1;
    background: linear-gradient(170deg, var(--orange) 0%, var(--orange-deep) 60%, var(--rust) 100%);
    clip-path: polygon(0 6%, 22% 0, 48% 22%, 70% 30%, 100% 40%, 100% 100%, 0 100%);
  }
  .bread-art {
    position: absolute;
    right: 14px;
    bottom: 22px;
    width: 124px;
    height: 100px;
    z-index: 3;
    border-radius: 46% 46% 40% 40%;
    background: radial-gradient(ellipse at 45% 40%, #f6b968 0%, #e99a45 65%, #c7742c 100%);
  }
  .contact {
    position: absolute;
    left: 22px;
    bottom: 24px;
    z-index: 3;
    text-align: left;
    color: var(--white);
  }
  .contact-email {
    display: flex;
    align-items: center;
    gap: 7px;
    font-weight: 600;
    font-size: 11.5px;
  }
  .contact-email svg { width: 15px; height: 11px; }
  .contact-phone {
    font-weight: 700;
    font-size: 27px;
    line-height: 1.15;
  }
</style>
</head>
<body>
<main class="sheet">

  <section class="panel front">
    <div class="content">
      <h1 class="script-title">The transformation of bread</h1>
      <div class="brand"><span class="brand-dot"></span><span class="brand-name">Tidal Crumb</span></div>
      <h2 class="headline">NUTRITIOUS DIGESTIBLE DELICIOUS</h2>
      <p class="subline">An alternative to the mutated genetics of modern wheat</p>
      <h3 class="section-label">Sprouted grains:</h3>
      <p class="section-text">Einkorn, spelt, and a touch of heritage rye (Organically grown on family farms in Winthrop, Washington and Teton Valley, Idaho)</p>
      <h3 class="section-label">Seeds:</h3>
      <p class="section-text">Amaranth, sprouted pumpkin seeds, sprouted quinoa, chia seeds, flaxseed, hemp hearts, sprouted sunflowers seeds</p>
      <div class="split">
        <div class="split-col"><h3 class="section-label">Adaptogens:</h3><p class="section-text">Ashwaganda, Maca root</p></div>
        <div class="split-divider"></div>
        <div class="split-col"><h3 class="section-label">Mushroom extracts:</h3><p class="section-text">Lions mane, cordycept</p></div>
      </div>
      <p class="extras">With: Montana glacier well water, Cacao, MCT oil, psyllium husk, Himalayan sea salt, trace minerals, &nbsp;love</p>
      <p class="tolerance">This bread is well tolerated by people with gluten sensitivities.</p>
      <p class="note">(not for celiac disease)</p>
    </div>
    <div class="landscape" role="img" aria-label="Illustrated orange desert hills landscape"></div>
    <div class="bread-art" role="img" aria-label="Illustration of two slices of toasted bread"></div>
    <div class="contact">
      <p class="contact-email"><svg viewBox="0 0 30 22" aria-hidden="true"><rect width="30" height="22" rx="2" fill="#fff"/><polyline points="1,2 15,13 29,2" fill="none" stroke="#e8702a" stroke-width="2.4"/></svg>hello@tidalcrumb.com</p>
      <p class="contact-phone">406-555-0148</p>
    </div>
  </section>

  <section class="panel back">
    <div class="content">
      <h1 class="script-title">The transformation of bread</h1>
      <div class="brand"><span class="brand-dot"></span><span class="brand-name">Tidal Crumb</span></div>
      <h2 class="headline">EINKORN GRAIN VS 'MODERN WHEAT'</h2>
      <p class="intro"><strong>Einkorn</strong> is the original, non-altered wheat grain.<br>It's genetic purity is over 10,000 years old.</p>
      <h3 class="section-label">Einkorn is:</h3>
      <ul class="benefits">
        <li><svg viewBox="0 0 10 10" aria-hidden="true"><polyline points="1,5 4,8 9,1" fill="none" stroke="#e8a04c" stroke-width="2"/></svg>25% higher in protein and lower in carbohydrates than modern wheat</li>
        <li><svg viewBox="0 0 10 10" aria-hidden="true"><polyline points="1,5 4,8 9,1" fill="none" stroke="#e8a04c" stroke-width="2"/></svg>3-4 times more beta-carotene</li>
        <li><svg viewBox="0 0 10 10" aria-hidden="true"><polyline points="1,5 4,8 9,1" fill="none" stroke="#e8a04c" stroke-width="2"/></svg>2 times more vitamin A</li>
        <li><svg viewBox="0 0 10 10" aria-hidden="true"><polyline points="1,5 4,8 9,1" fill="none" stroke="#e8a04c" stroke-width="2"/></svg>4 times more antioxidants lutein and riboflavin.</li>
        <li><svg viewBox="0 0 10 10" aria-hidden="true"><polyline points="1,5 4,8 9,1" fill="none" stroke="#e8a04c" stroke-width="2"/></svg>5-6 times more expensive $$$</li>
        <li><svg viewBox="0 0 10 10" aria-hidden="true"><polyline points="1,5 4,8 9,1" fill="none" stroke="#e8a04c" stroke-width="2"/></svg>richer in carotenoids, B vitamins, and essential and trace minerals</li>
        <li><svg viewBox="0 0 10 10" aria-hidden="true"><polyline points="1,5 4,8 9,1" fill="none" stroke="#e8a04c" stroke-width="2"/></svg>non-processed, non-hybridized, non-GMO, non-mutated and has a low glycemic load, meaning it won't spike your blood sugar level.</li>
        <li><svg viewBox="0 0 10 10" aria-hidden="true"><polyline points="1,5 4,8 9,1" fill="none" stroke="#e8a04c" stroke-width="2"/></svg>and it tastes better.</li>
      </ul>
      <p class="gluten-box">Einkorn lacks the gluten proteins that trigger symptoms of gluten sensitivity.</p>
    </div>
    <div class="landscape" role="img" aria-label="Illustrated orange desert hills landscape"></div>
    <div class="bread-art" role="img" aria-label="Illustration of two slices of toasted bread"></div>
    <div class="contact">
      <p class="contact-email"><svg viewBox="0 0 30 22" aria-hidden="true"><rect width="30" height="22" rx="2" fill="#fff"/><polyline points="1,2 15,13 29,2" fill="none" stroke="#e8702a" stroke-width="2.4"/></svg>hello@tidalcrumb.com</p>
      <p class="contact-phone">406-555-0148</p>
    </div>
  </section>

  <section class="panel front">
    <div class="content">
      <h1 class="script-title">The transformation of bread</h1>
      <div class="brand"><span class="brand-dot"></span><span class="brand-name">Tidal Crumb</span></div>
      <h2 class="headline">NUTRITIOUS DIGESTIBLE DELICIOUS</h2>
      <p class="subline">An alternative to the mutated genetics of modern wheat</p>
      <h3 class="section-label">Sprouted grains:</h3>
      <p class="section-text">Einkorn, spelt, and a touch of heritage rye (Organically grown on family farms in Winthrop, Washington and Teton Valley, Idaho)</p>
      <h3 class="section-label">Seeds:</h3>
      <p class="section-text">Amaranth, sprouted pumpkin seeds, sprouted quinoa, chia seeds, flaxseed, hemp hearts, sprouted sunflowers seeds</p>
      <div class="split">
        <div class="split-col"><h3 class="section-label">Adaptogens:</h3><p class="section-text">Ashwaganda, Maca root</p></div>
        <div class="split-divider"></div>
        <div class="split-col"><h3 class="section-label">Mushroom extracts:</h3><p class="section-text">Lions mane, cordycept</p></div>
      </div>
      <p class="extras">With: Montana glacier well water, Cacao, MCT oil, psyllium husk, Himalayan sea salt, trace minerals, &nbsp;love</p>
      <p class="tolerance">This bread is well tolerated by people with gluten sensitivities.</p>
      <p class="note">(not for celiac disease)</p>
    </div>
    <div class="landscape" role="img" aria-label="Illustrated orange desert hills landscape"></div>
    <div class="bread-art" role="img" aria-label="Illustration of two slices of toasted bread"></div>
    <div class="contact">
      <p class="contact-email"><svg viewBox="0 0 30 22" aria-hidden="true"><rect width="30" height="22" rx="2" fill="#fff"/><polyline points="1,2 15,13 29,2" fill="none" stroke="#e8702a" stroke-width="2.4"/></svg>hello@tidalcrumb.com</p>
      <p class="contact-phone">406-555-0148</p>
    </div>
  </section>

  <section class="panel back">
    <div class="content">
      <h1 class="script-title">The transformation of bread</h1>
      <div class="brand"><span class="brand-dot"></span><span class="brand-name">Tidal Crumb</span></div>
      <h2 class="headline">EINKORN GRAIN VS 'MODERN WHEAT'</h2>
      <p class="intro"><strong>Einkorn</strong> is the original, non-altered wheat grain.<br>It's genetic purity is over 10,000 years old.</p>
      <h3 class="section-label">Einkorn is:</h3>
      <ul class="benefits">
        <li><svg viewBox="0 0 10 10" aria-hidden="true"><polyline points="1,5 4,8 9,1" fill="none" stroke="#e8a04c" stroke-width="2"/></svg>25% higher in protein and lower in carbohydrates than modern wheat</li>
        <li><svg viewBox="0 0 10 10" aria-hidden="true"><polyline points="1,5 4,8 9,1" fill="none" stroke="#e8a04c" stroke-width="2"/></svg>3-4 times more beta-carotene</li>
        <li><svg viewBox="0 0 10 10" aria-hidden="true"><polyline points="1,5 4,8 9,1" fill="none" stroke="#e8a04c" stroke-width="2"/></svg>2 times more vitamin A</li>
        <li><svg viewBox="0 0 10 10" aria-hidden="true"><polyline points="1,5 4,8 9,1" fill="none" stroke="#e8a04c" stroke-width="2"/></svg>4 times more antioxidants lutein and riboflavin.</li>
        <li><svg viewBox="0 0 10 10" aria-hidden="true"><polyline points="1,5 4,8 9,1" fill="none" stroke="#e8a04c" stroke-width="2"/></svg>5-6 times more expensive $$$</li>
        <li><svg viewBox="0 0 10 10" aria-hidden="true"><polyline points="1,5 4,8 9,1" fill="none" stroke="#e8a04c" stroke-width="2"/></svg>richer in carotenoids, B vitamins, and essential and trace minerals</li>
        <li><svg viewBox="0 0 10 10" aria-hidden="true"><polyline points="1,5 4,8 9,1" fill="none" stroke="#e8a04c" stroke-width="2"/></svg>non-processed, non-hybridized, non-GMO, non-mutated and has a low glycemic load, meaning it won't spike your blood sugar level.</li>
        <li><svg viewBox="0 0 10 10" aria-hidden="true"><polyline points="1,5 4,8 9,1" fill="none" stroke="#e8a04c" stroke-width="2"/></svg>and it tastes better.</li>
      </ul>
      <p class="gluten-box">Einkorn lacks the gluten proteins that trigger symptoms of gluten sensitivity.</p>
    </div>
    <div class="landscape" role="img" aria-label="Illustrated orange desert hills landscape"></div>
    <div class="bread-art" role="img" aria-label="Illustration of two slices of toasted bread"></div>
    <div class="contact">
      <p class="contact-email"><svg viewBox="0 0 30 22" aria-hidden="true"><rect width="30" height="22" rx="2" fill="#fff"/><polyline points="1,2 15,13 29,2" fill="none" stroke="#e8702a" stroke-width="2.4"/></svg>hello@tidalcrumb.com</p>
      <p class="contact-phone">406-555-0148</p>
    </div>
  </section>

</main>
</body>
</html>
```